New business needs it's first website designed and coded for Wordpress

This is a new website for a new business. The business is called The Remote Tech Specialist (TRTS). The business is based across multiple countries with the goal of providing workers in the Philippines opportunities to find work in international companies based in Australia, Singapore and New Zealand. The target market for TRTS is large enterprises (initially in Australia) looking for well legally structured business that knows how to recruit the top IT professionals and ensure that they are happy, all compliance, taxes and legals and professionally done and all services contracts are local to ensure enforceability.

We are looking for 10 pages (6 templates) for the website as follows:
Home
About Us
Services
Work from home full-timers
Work from office full-times
Work from home contractors
Work from office contractors
Careers Job Search
Employers Contact Us
Candidates Register your interest

Target Market(s)

IT Professionals in the Philippines & large enterprises in Australia, Singapore and New Zealand

Industry/Entity Type

IT Recruitment

Coding

Number of Pages Required

5+ page

Requirements
Must have
• Please based style off logo file attached.

```html
<!DOCTYPE html>
<html lang="en">
<head>
<meta charset="utf-8">
<title>TRTS – The Remote Tech Specialist</title>
<link href="https://fonts.googleapis.com/css2?family=Michroma&family=Montserrat:wght@400;500;600;700&display=swap" rel="stylesheet">
<style>
:root{
  --blue:#1591e6;
  --blue-dark:#0b6fc0;
  --ink:#0b0d12;
  --navy:#151c28;
  --grey:#d4d4d4;
  --pale:#e3edf5;
  --text:#2b2f36;
  --muted:#5b6270;
  --white:#ffffff;
  --line:#d9dde3;
}
*{box-sizing:border-box;margin:0;padding:0}
html,body{width:1200px;height:4338px;overflow:hidden}
body{position:relative;background:var(--white);font-family:"Montserrat",sans-serif;color:var(--text)}
.abs{position:absolute}
.display{font-family:"Michroma",sans-serif;font-weight:400;letter-spacing:.5px;-webkit-text-stroke:.7px currentColor}
.accent{color:var(--blue)}
.btn{position:absolute;background:var(--blue);color:var(--white);font-family:"Michroma",sans-serif;font-size:15px;display:flex;align-items:center;justify-content:center;border-radius:4px;-webkit-text-stroke:.4px currentColor}

/* Hero */
.hero-bg{position:absolute;left:0;top:0;width:1200px;height:720px}
.topline{position:absolute;left:0;top:0;width:1200px;height:4px;background:var(--blue)}
.brand{position:absolute;display:flex;align-items:center;gap:10px;color:var(--white)}
.brand-name{font-family:"Michroma",sans-serif;font-size:34px;line-height:1}
.brand-sub{font-family:"Montserrat",sans-serif;font-size:12px;line-height:1.05;border-left:2px solid var(--white);padding-left:6px;text-transform:uppercase}
.nav{position:absolute;left:372px;top:44px;display:flex;gap:21px;color:var(--white);font-size:14px;font-weight:500}
.nav .active{text-decoration:underline;text-underline-offset:5px;font-weight:600}
.hero-title{left:64px;top:196px;color:var(--white);font-size:33px;line-height:43px}
.hero-copy{left:64px;top:334px;width:400px;color:var(--white);font-size:14px;line-height:24px;font-weight:600}

/* About */
.about-photo{left:130px;top:735px;width:414px;height:414px;border-radius:50%;background:radial-gradient(circle at 45% 40%,#8a7a66,#4a4640 55%,#22252b)}
.about h2{left:641px;top:760px;font-size:31px;color:var(--ink)}
.about p{position:absolute;left:641px;width:455px;font-size:14px;line-height:22.5px;color:var(--text)}

/* Services */
.services-title{left:0;width:1200px;top:1326px;text-align:center;color:var(--white);font-size:31px}
.services-lead{left:230px;width:740px;top:1381px;text-align:center;color:#dfe6ee;font-size:14px;line-height:22px}
.svc-card{position:absolute;top:1495px;width:340px;height:284px;border:1.5px solid var(--blue-dark);border-radius:8px}
.svc-icon{position:absolute;left:24px;top:-34px;width:78px;height:70px;border-radius:6px;background:var(--blue);display:flex;align-items:center;justify-content:center}
.svc-card h3{position:absolute;left:26px;top:70px;color:var(--white);font-family:"Michroma",sans-serif;font-weight:400;font-size:17px;-webkit-text-stroke:.5px currentColor}
.svc-card p{position:absolute;left:26px;top:112px;width:290px;color:#d9e0e8;font-size:14px;line-height:23px}
.svc-card .more{position:absolute;left:26px;top:222px;color:var(--blue);font-family:"Michroma",sans-serif;font-size:14px;text-decoration:underline}

/* Partners */
.partners-title{left:0;width:1200px;top:2020px;text-align:center;font-size:30px;color:var(--ink)}
.partners{position:absolute;left:103px;top:2099px;width:999px;height:162px;display:grid;grid-template-columns:repeat(4,1fr);grid-template-rows:repeat(2,1fr);border:1px solid var(--line)}
.partner{display:flex;align-items:center;justify-content:center;gap:10px;border-right:1px solid var(--line);border-bottom:1px solid var(--line);font-size:19px;font-weight:500;color:#3a3f47}
.partner:nth-child(4n){border-right:none}
.partner:nth-child(n+5){border-bottom:none}
.partner .dot{width:22px;height:22px;border-radius:50%;background:#8b9099}
.partner.featured{box-shadow:0 4px 14px rgba(0,0,0,.18);border:1.5px solid var(--blue);position:relative;z-index:1}

/* Consulting */
.consult-title{left:0;width:1200px;top:2474px;text-align:center;font-size:30px;color:var(--ink)}
.c-card{position:absolute;width:320px;height:302px;background:var(--white);border-radius:10px;box-shadow:0 2px 6px rgba(0,0,0,.14);border:1px solid #edf0f3}
.c-card.lifted{border-bottom:4px solid var(--blue)}
.c-icon{position:absolute;left:30px;top:24px;width:58px;height:58px;border-radius:50%;background:#bfe3f7;display:flex;align-items:center;justify-content:center}
.c-card h3{position:absolute;left:30px;top:108px;font-size:20px;font-weight:600;color:var(--ink)}
.c-card p{position:absolute;left:30px;top:148px;width:262px;font-size:14px;line-height:22px;color:var(--text)}
.c-card .more{position:absolute;left:32px;top:248px;font-size:14px;font-weight:600;color:var(--blue);text-decoration:underline}

/* Contact form */
.contact-title{left:0;width:1200px;top:3404px;text-align:center;font-size:30px;color:var(--ink)}
.field{position:absolute;border:1px solid #cfd3d9;border-radius:3px;font-size:13px;color:#4d525a;padding:13px 14px;background:var(--white)}

/* Footer */
.footer-col h4{position:absolute;color:var(--white);font-family:"Michroma",sans-serif;font-weight:400;font-size:17px;-webkit-text-stroke:.4px currentColor}
.flinks{position:absolute;left:329px;top:4068px;color:#e2e6ec;font-size:14px;line-height:29px;list-style:none}
.vrule{position:absolute;width:2px;background:#e8e8e8}
.cinfo{position:absolute;left:557px;color:var(--white);font-size:12px;line-height:17px}
.cinfo b{display:block;font-size:14px;font-weight:700}
.cinfo-icon{position:absolute;left:548px}
.newsletter{position:absolute;left:815px;top:4073px;width:272px;height:44px;background:var(--white);border-radius:2px;font-size:13px;color:#4d525a;padding:13px 16px}
.social{position:absolute;top:4139px;width:36px;height:36px;border-radius:50%;border:1.5px solid var(--white)}
.copyright{left:0;width:1200px;top:4290px;text-align:center;color:var(--white);font-size:13px}
</style>
</head>
<body>

<!-- HERO -->
<svg class="hero-bg" viewBox="0 0 1200 720" aria-hidden="true">
  <defs>
    <linearGradient id="heroShade" x1="0" y1="0" x2="1" y2="1">
      <stop offset="0" stop-color="#0d1626"/>
      <stop offset=".55" stop-color="#1f3148"/>
      <stop offset="1" stop-color="#0a0f19"/>
    </linearGradient>
  </defs>
  <polygon points="0,0 1200,0 1200,590 0,645" fill="url(#heroShade)"/>
  <polygon points="240,634 1200,572 1200,590 855,614 240,652" fill="var(--grey)"/>
  <polygon points="855,614 1200,590 1200,712" fill="var(--blue)"/>
</svg>
<div class="abs" role="img" aria-label="Photo of smiling IT professionals working together on a tablet with data overlays" style="left:600px;top:0;width:600px;height:600px;background:radial-gradient(ellipse at 50% 35%,rgba(150,120,90,.55),rgba(40,60,85,.25) 55%,rgba(0,0,0,0) 75%)"></div>
<div class="topline"></div>
<div class="brand" style="left:65px;top:32px">
  <span class="brand-name">TRTS</span>
  <span class="brand-sub">The<br>Remote<br>Tech Specialist</span>
</div>
<nav class="nav">
  <span class="active">Home</span><span>About Us</span><span>Services</span><span>Work from home ⌄</span><span>Careers Job Search</span><span>Employers Contact Us</span><span>More ⌄</span>
</nav>
<h1 class="abs display hero-title">EMPOWERING YOUR<br>BUSINESS WITH EXPERT<br>IT VIRTUAL</h1>
<p class="abs hero-copy">Lorem ipsum dolor sit amet, consectetur adipiscing elit, sed do eiusmod tempor aliqua.</p>
<div class="btn" style="left:66px;top:400px;width:152px;height:42px">GET STARTED</div>

<!-- ABOUT -->
<section class="about">
  <div class="abs about-photo" role="img" aria-label="Photo of a team meeting around a table in a modern office"></div>
  <h2 class="abs display"><span class="accent">ABOUT</span> TRTS</h2>
  <p style="top:810px">Lorem ipsum dolor sit amet, consectetur adipiscing elit, sed do eiusmod tempor incididunt ut labore et dolore magna aliqua. Ut enim ad minim veniam, quis nostrud exercitation ullamco laboris nisi ut aliquip ex ea commodo consequat.</p>
  <p style="top:906px">Sed ut perspiciatis unde omnis iste natus error sit voluptatem accusantium doloremque laudantium, totam rem aperiam, eaque ipsa quae ab illo inventore veritatis et quasi architecto beatae vitae dicta sunt explicabo. Nemo enim ipsam voluptatem quia voluptas sit aspernatur aut odit aut fugit, sed quia consequuntur magni dolores eos qui ratione voluptatem sequi nesciunt.</p>
  <div class="btn" style="left:641px;top:1071px;width:154px;height:42px">READ MORE</div>
</section>

<!-- SERVICES -->
<svg class="abs" style="left:0;top:1168px" width="1200" height="780" viewBox="0 0 1200 780" role="img" aria-label="Dark office photo backdrop">
  <defs>
    <linearGradient id="svcShade" x1="0" y1="0" x2="0" y2="1">
      <stop offset="0" stop-color="#1a2638"/>
      <stop offset=".5" stop-color="#1d2a3d"/>
      <stop offset="1" stop-color="#1c1f26"/>
    </linearGradient>
  </defs>
  <polygon points="0,65 1200,0 1200,660 0,777" fill="url(#svcShade)"/>
</svg>
<h2 class="abs display services-title"><span class="accent">OUR</span> SERVICES</h2>
<p class="abs services-lead">Lorem ipsum dolor sit amet, consectetur adipiscing elit, sed do eiusmod tempor incididunt ut labore et dolore magna aliqua.</p>

<div class="svc-card" style="left:76px">
  <div class="svc-icon"><svg width="40" height="40" viewBox="0 0 40 40" fill="none" stroke="#fff" stroke-width="2"><circle cx="20" cy="16" r="8"/><circle cx="20" cy="16" r="3"/><path d="M6 32h28M10 27l6 5"/></svg></div>
  <h3>LOREM IPSUM</h3>
  <p>Lorem ipsum dolor sit amet, consectetur adipiscing elit, sed do eiusmod tempor incididunt ut labore et dolore magna aliqua.</p>
  <span class="more">READ MORE</span>
</div>
<div class="svc-card" style="left:434px">
  <div class="svc-icon"><svg width="40" height="40" viewBox="0 0 40 40" fill="none" stroke="#fff" stroke-width="2"><rect x="6" y="8" width="28" height="22" rx="2"/><path d="M6 14h28M14 20l-3 3 3 3M22 20l3 3-3 3"/></svg></div>
  <h3>LOREM IPSUM</h3>
  <p>Lorem ipsum dolor sit amet, consectetur adipiscing elit, sed do eiusmod tempor incididunt ut labore et dolore magna aliqua.</p>
  <span class="more">READ MORE</span>
</div>
<div class="svc-card" style="left:793px">
  <div class="svc-icon"><svg width="40" height="40" viewBox="0 0 40 40" fill="none" stroke="#fff" stroke-width="2"><circle cx="16" cy="16" r="6"/><path d="M6 34c0-7 4-11 10-11s10 4 10 11"/><circle cx="29" cy="11" r="5"/></svg></div>
  <h3>LOREM IPSUM</h3>
  <p>Lorem ipsum dolor sit amet, consectetur adipiscing elit, sed do eiusmod tempor incididunt ut labore et dolore magna aliqua.</p>
  <span class="more">READ MORE</span>
</div>

<!-- PARTNERS -->
<h2 class="abs display partners-title"><span class="accent">THE REMOTE TECH</span> PARTNERS</h2>
<div class="partners">
  <div class="partner"><span class="dot"></span>Corelane</div>
  <div class="partner">Brightgrid</div>
  <div class="partner">Northwire</div>
  <div class="partner">Halcyon Group</div>
  <div class="partner">Stackwell</div>
  <div class="partner featured"><span class="dot"></span>Pinecrest IT</div>
  <div class="partner">Veltrix</div>
  <div class="partner">Orbis Digital</div>
</div>

<!-- IT CONSULTING -->
<svg class="abs" style="left:0;top:2338px" width="1200" height="1005" viewBox="0 0 1200 1005" aria-hidden="true">
  <polygon points="0,52 1200,0 1200,944 0,1002" fill="var(--pale)"/>
</svg>
<h2 class="abs display consult-title"><span class="accent">IT</span> CONSULTING</h2>

<div class="c-card" style="left:103px;top:2553px">
  <div class="c-icon"><svg width="34" height="34" viewBox="0 0 34 34" fill="none" stroke="#1c2738" stroke-width="2"><circle cx="13" cy="10" r="5"/><path d="M3 30c0-7 4-11 10-11s10 4 10 11"/><rect x="20" y="18" width="12" height="9"/></svg></div>
  <h3>Advisory Services</h3>
  <p>Lorem ipsum dolor sit amet consctetaur adipiscing elit sett do temporeausarmod incidunt ut labore dolore</p>
  <span class="more">Read More</span>
</div>
<div class="c-card lifted" style="left:439px;top:2553px">
  <div class="c-icon"><svg width="34" height="34" viewBox="0 0 34 34" fill="none" stroke="#1c2738" stroke-width="2"><rect x="6" y="5" width="18" height="24" rx="2"/><path d="M10 12h10M10 17h10M10 22h6"/><circle cx="26" cy="24" r="5"/></svg></div>
  <h3>Health Check Services</h3>
  <p>Lorem ipsum dolor sit amet consctetaur adipiscing elit sett do temporeausarmod incidunt ut labore dolore</p>
  <span class="more">Read More</span>
</div>
<div class="c-card" style="left:776px;top:2553px">
  <div class="c-icon"><svg width="34" height="34" viewBox="0 0 34 34" fill="none" stroke="#1c2738" stroke-width="2"><rect x="5" y="10" width="24" height="18"/><path d="M5 10l4-5h16l4 5M12 16v8M17 16v8M22 16v8"/></svg></div>
  <h3>Statements of Work</h3>
  <p>Lorem ipsum dolor sit amet consctetaur adipiscing elit sett do temporeausarmod incidunt ut labore dolore</p>
  <span class="more">Read More</span>
</div>
<div class="c-card" style="left:103px;top:2876px">
  <div class="c-icon"><svg width="34" height="34" viewBox="0 0 34 34" fill="none" stroke="#1c2738" stroke-width="2"><rect x="5" y="8" width="24" height="17" rx="2"/><path d="M12 30h10M17 25v5"/><circle cx="17" cy="16" r="4"/></svg></div>
  <h3>Block of Hours</h3>
  <p>Lorem ipsum dolor sit amet consctetaur adipiscing elit sett do temporeausarmod incidunt ut labore dolore</p>
  <span class="more">Read More</span>
</div>
<div class="c-card" style="left:439px;top:2876px">
  <div class="c-icon"><svg width="34" height="34" viewBox="0 0 34 34" fill="none" stroke="#1c2738" stroke-width="2"><circle cx="14" cy="14" r="7"/><path d="M11 24h6M12 28h4"/><circle cx="25" cy="22" r="5"/></svg></div>
  <h3>Project Management</h3>
  <p>Lorem ipsum dolor sit amet consctetaur adipiscing elit sett do temporeausarmod incidunt ut labore dolore</p>
  <span class="more">Read More</span>
</div>
<div class="c-card" style="left:776px;top:2876px">
  <div class="c-icon"><svg width="34" height="34" viewBox="0 0 34 34" fill="none" stroke="#1c2738" stroke-width="2"><circle cx="9" cy="8" r="3"/><circle cx="25" cy="8" r="3"/><path d="M4 17c0-3 2-5 5-5s5 2 5 5M20 17c0-3 2-5 5-5s5 2 5 5M13 24h8l-3-3M21 28h-8l3 3"/></svg></div>
  <h3>Scheduled Engagement</h3>
  <p>Lorem ipsum dolor sit amet consctetaur adipiscing elit sett do temporeausarmod incidunt ut labore dolore</p>
  <span class="more">Read More</span>
</div>

<!-- GET IN TOUCH -->
<h2 class="abs display contact-title"><span class="accent">GET</span> IN TOUCH</h2>
<div class="field" style="left:194px;top:3467px;width:264px;height:45px">Full Name</div>
<div class="field" style="left:468px;top:3467px;width:263px;height:45px">Phone</div>
<div class="field" style="left:742px;top:3467px;width:264px;height:45px">Email Address</div>
<div class="field" style="left:194px;top:3524px;width:812px;height:192px">Message</div>
<div class="btn" style="left:523px;top:3743px;width:154px;height:42px">SUBMIT</div>

<!-- FOOTER -->
<svg class="abs" style="left:0;top:3780px" width="1200" height="558" viewBox="0 0 1200 558" aria-hidden="true">
  <polygon points="0,0 0,125 345,98" fill="var(--blue)"/>
  <polygon points="0,125 960,58 960,76 0,145" fill="var(--grey)"/>
  <polygon points="0,145 960,76 1200,60 1200,558 0,558" fill="var(--ink)"/>
</svg>
<div class="brand" style="left:59px;top:4093px;width:222px;height:64px;background:#000;justify-content:center">
  <span class="brand-name" style="font-size:28px">TRTS</span>
  <span class="brand-sub" style="font-size:10px">The<br>Remote<br>Tech Specialist</span>
</div>
<div class="vrule" style="left:301px;top:4012px;height:70px"></div>
<div class="vrule" style="left:523px;top:4012px;height:250px;width:1px"></div>
<div class="vrule" style="left:770px;top:4012px;height:250px;width:1px"></div>
<div class="vrule" style="left:523px;top:4012px;height:36px"></div>
<div class="vrule" style="left:770px;top:4012px;height:36px"></div>
<div class="footer-col"><h4 style="left:326px;top:4024px">QUICK LINKS</h4></div>
<ul class="flinks">
  <li>Home</li><li>About Us</li><li>Services</li><li>Work from home ⌄</li><li>Careers Job Search</li><li>Employers Contact Us</li><li>More ⌄</li>
</ul>
<div class="footer-col"><h4 style="left:547px;top:4024px">CONTACT INFO</h4></div>
<svg class="cinfo-icon" style="top:4076px" width="12" height="14" viewBox="0 0 12 14"><path d="M6 0a5 5 0 0 0-5 5c0 4 5 9 5 9s5-5 5-9a5 5 0 0 0-5-5z" fill="#fff"/><circle cx="6" cy="5" r="2" fill="#0b0d12"/></svg>
<div class="cinfo" style="left:584px;top:4072px;width:180px"><b>ADDRESS:</b>465, Lorum Ipsum Dolore Sed, Australia</div>
<svg class="cinfo-icon" style="top:4142px" width="13" height="13" viewBox="0 0 13 13"><path d="M3 0l2 3-1.5 1.5a8 8 0 0 0 5 5L10 8l3 2-1.5 3C6 13 0 7 0 1.5z" fill="#fff"/></svg>
<div class="cinfo" style="left:584px;top:4138px"><b>PHONE:</b>+61 (02) 5550 0142</div>
<svg class="cinfo-icon" style="top:4200px" width="14" height="11" viewBox="0 0 14 11"><rect width="14" height="11" fill="#fff"/><path d="M0 0l7 6 7-6" stroke="#0b0d12" fill="none"/></svg>
<div class="cinfo" style="left:584px;top:4196px"><b>EMAIL:</b>hello@trts-mail.com</div>
<div class="footer-col"><h4 style="left:808px;top:4024px">SIGN UP TO OUR NEWSLETTER</h4></div>
<div class="newsletter">Email Address</div>
<svg class="abs" style="left:1053px;top:4086px" width="18" height="18" viewBox="0 0 18 18"><path d="M1 8l16-7-6 16-3-6z" fill="var(--blue)"/></svg>
<div class="social" style="left:815px" aria-label="Social profile"></div>
<div class="social" style="left:857px" aria-label="Social profile"></div>
<div class="social" style="left:899px" aria-label="Social profile"></div>
<div class="abs" style="left:96px;top:4270px;width:1008px;height:1px;background:#3a3d44"></div>
<p class="abs copyright">© 2024 The Remote Tech Specialist | All Rights Reserved</p>

</body>
</html>
```